Productos de Embalaje, todo lo que necesitas en un solo lugar.

Hola, somos una empresa ubicada en Monterrey, México, comercializamos productos empaques industriales, de entrada no se si quiera si el titulo del proyecto es el correcto, este saldrá supongo en el folleto?, no sé si necesitamos un brochure o un flyer, no se las diferencias, por eso me acerco a ustedes, soy malo para el diseño.

Favor de basarse en nuestra página web www.brivo-lum.com, de ahi se pueden sacar textos, colores, etc, adjunto logo, imagenes que pueden servirles de nuestros productos, así como un ejemplo de brochure que vi, se ve padre.

Quiero hacer crecer mi negocio y buscar clientes potenciales por correo principalmente. así como presencial, por lo que se requiere enviarse por correo o imprimir, el proyecto es 100% español.

Queremos algo atractivo, fresco, profesional

____________________________________________

Hello, we are a micro company located in Monterrey, Mexico, I do not know if we need a brochure or a flyer, we specialize in marketing products for Industrial Packaging, I want to grow my business and look for potential customers by mail mainly, as well as face-to-face, by What this design is required can be sent by mail or printed, we want something eye-catching, fresh, professional.
Our web page is www.brivo-lum.com , already attach a brochure example that is good.

Target Market(s)

Clientes de habla hispana, favor de checar mi página www.brivo-lum.com

Industry/Entity Type

Industrial

Requirements
Must have
• Contacto:
• Teléfono: (81) 8157-6203
• Correo: ventas@brivo-lum.com
• Monterrey, Nuevo León, México.
• instagram y facebook
• @BRIVOLUMX
• @brivolumx
Nice to have
• Estoy abierto, proporcione un brochure de ejemplo que me gusto, pero acepto diseños diferentes, www.brivo-lum.com
Should not have
• English.

```html
<!DOCTYPE html>
<html lang="es">
<head>
<meta charset="utf-8">
<title>BRIVO-LUM · Empaque Industrial</title>
<link href="https://fonts.googleapis.com/css2?family=Oswald:wght@400;500;600&family=Open+Sans:wght@400;600;700&display=swap" rel="stylesheet">
<style>
  :root{
    --stage:#4a4a4a;
    --paper:#ffffff;
    --orange:#e5a23a;
    --orange-deep:#e09a2c;
    --ink:#1e1e1e;
    --grey-text:#7d7d7d;
    --panel:#ececec;
    --tile-border:#cfcfcf;
  }
  *{box-sizing:border-box;margin:0;padding:0}
  html,body{width:1200px;height:1200px;overflow:hidden;background:var(--stage)}
  body{position:relative;font-family:"Open Sans",Arial,sans-serif;color:var(--ink)}
  .page{position:absolute;top:303px;width:424px;height:594px;background:var(--paper)}
  .page--front{left:129px}
  .page--back{left:647px}
  .abs{position:absolute}

  .brand{text-align:center}
  .brand__name{font-family:"Oswald",sans-serif;font-weight:600;font-size:31px;line-height:1;color:var(--grey-text);letter-spacing:-.5px}
  .brand__tag{font-size:7.5px;color:var(--grey-text);letter-spacing:.5px;margin-top:2px}

  .rule{left:17px;top:69px;width:393px;height:3px;background:var(--orange)}
  .photo{border:0}

  .welcome{font-family:"Oswald",sans-serif;font-weight:500;font-size:28px;line-height:1;color:var(--orange);letter-spacing:-.5px}
  .h-orange{font-family:"Open Sans",sans-serif;font-weight:700;font-size:11.5px;color:var(--orange);line-height:1.2}
  .body-copy{font-size:6.3px;line-height:1.45;text-align:justify;color:#222}

  .info-panel{left:214px;top:287px;width:196px;height:274px;background:var(--panel)}
  .values{display:grid;grid-template-columns:1fr 1fr;row-gap:5px;font-size:6.6px;font-weight:600}
  .values li{list-style:none;display:flex;align-items:center;gap:4px}
  .tick{width:6px;height:6px}

  .slogan{font-family:"Oswald",sans-serif;font-weight:500;line-height:1.1;letter-spacing:-.2px}
  .slogan__line1{color:var(--ink)}
  .slogan__line2{color:var(--orange)}
  .contact{display:flex;align-items:center;gap:4px;white-space:nowrap}
  .contact__phone{font-weight:700;color:var(--ink)}
  .contact__mail{font-size:6.6px;color:#333}

  .footer{left:17px;width:393px;height:25px;background:var(--orange);display:flex;align-items:center;justify-content:space-between;padding:0 7px;font-size:6.8px;color:#1d1d1d}
  .footer span{display:flex;align-items:center;gap:3px}
  .dot{width:7px;height:7px;border-radius:50%;background:#1d1d1d;display:inline-block}

  .products-head{left:17px;top:17px;width:393px;height:44px;background:var(--panel);display:flex;align-items:center;justify-content:center;font-weight:700;font-size:19px;color:var(--orange);letter-spacing:.3px}
  .tile{border:1px solid var(--tile-border)}
  .divider{width:2px;background:var(--orange)}
</style>
</head>
<body>

<!-- Front page -->
<section class="page page--front">
  <div class="abs brand" style="left:0;width:424px;top:17px">
    <div class="brand__name">BRIVO-LUM</div>
    <div class="brand__tag">Empaque Industrial</div>
  </div>
  <div class="abs rule"></div>

  <div class="abs photo" role="img" aria-label="Guantes industriales de protección apilados" style="left:17px;top:72px;width:277px;height:215px;background:linear-gradient(160deg,#e8e6e0,#c9c6bd 50%,#d9b15a 80%,#e0ddd6)"></div>
  <div class="abs photo" role="img" aria-label="Rollo de cartón corrugado" style="left:300px;top:72px;width:110px;height:51px;background:linear-gradient(135deg,#8b6b45,#c8a77a)"></div>
  <div class="abs photo" role="img" aria-label="Plástico de burbuja" style="left:300px;top:127px;width:110px;height:51px;background:linear-gradient(135deg,#9a9a9a,#dcdcdc)"></div>
  <div class="abs photo" role="img" aria-label="Plástico de burbuja en primer plano" style="left:300px;top:182px;width:110px;height:51px;background:linear-gradient(135deg,#2e2e2e,#9a9a9a)"></div>
  <div class="abs photo" role="img" aria-label="Madera apilada" style="left:300px;top:237px;width:110px;height:50px;background:linear-gradient(135deg,#d9a57e,#b87a55)"></div>

  <div class="abs" style="left:17px;top:296px;width:188px">
    <div class="welcome">¡BIENVENIDO!</div>
    <p class="body-copy" style="margin-top:4px">En BRIVO-LUM somos una empresa dedicada a satisfacer las necesidades de la industria con soluciones para empaque, nuestros clientes obtienen ahorros importantes sin sacrificar la calidad de los productos.</p>
    <div class="h-orange" style="margin-top:8px;font-size:12px">MÁS INFORMACIÓN</div>
    <div class="h-orange" style="margin-top:5px">EMPRESA</div>
    <p class="body-copy" style="margin-top:2px">En BRIVO-LUM somos una empresa dedicada principalmente a la comercialización de productos de empaque industrial, con la idea de brindar precios muy competitivos en el mercado, logrando siempre mantener la calidad de nuestros productos, así como sus procesos formando un grupo de trabajo enfocado a la calidad, al servicio al cliente y sobre todo a la excelencia.</p>
    <div class="h-orange" style="margin-top:8px">VISIÓN</div>
    <p class="body-copy" style="margin-top:2px">Ser líderes a nivel nacional en la comercialización de productos para empaque industrial, ser reconocidos por la calidad de los productos que ofrecemos y el excelente servicio de nuestro personal, logrando incrementar nuestro servicio a un mayor número de clientes a través de una búsqueda continua de productos que satisfagan la demanda de la industria.</p>
  </div>

  <div class="abs info-panel"></div>
  <div class="abs" style="left:221px;top:296px;width:183px">
    <div class="h-orange">MISIÓN</div>
    <p class="body-copy" style="margin-top:2px">Responder a la confianza que nuestros clientes depositan en nosotros, buscando su entera satisfacción, así como también una relación duradera basada en el compromiso y respeto.</p>
    <div class="h-orange" style="margin-top:6px;font-size:12px">VALORES</div>
    <ul class="values" style="margin-top:4px">
      <li><svg class="tick" viewBox="0 0 10 10"><circle cx="5" cy="5" r="5" fill="#e5a23a"/><path d="M2.7 5.2l1.6 1.6 3-3.3" stroke="#fff" stroke-width="1.3" fill="none"/></svg>Calidad</li>
      <li><svg class="tick" viewBox="0 0 10 10"><circle cx="5" cy="5" r="5" fill="#e5a23a"/><path d="M2.7 5.2l1.6 1.6 3-3.3" stroke="#fff" stroke-width="1.3" fill="none"/></svg>Compromiso</li>
      <li><svg class="tick" viewBox="0 0 10 10"><circle cx="5" cy="5" r="5" fill="#e5a23a"/><path d="M2.7 5.2l1.6 1.6 3-3.3" stroke="#fff" stroke-width="1.3" fill="none"/></svg>Honestidad</li>
      <li><svg class="tick" viewBox="0 0 10 10"><circle cx="5" cy="5" r="5" fill="#e5a23a"/><path d="M2.7 5.2l1.6 1.6 3-3.3" stroke="#fff" stroke-width="1.3" fill="none"/></svg>Comunicación</li>
    </ul>
  </div>
  <div class="abs photo" role="img" aria-label="Rollo de espuma sobre piso de madera" style="left:217px;top:395px;width:190px;height:98px;background:linear-gradient(110deg,#9a6a3d 0%,#b88757 35%,#eeeeee 55%,#fafafa 100%)"></div>
  <div class="abs slogan" style="left:221px;top:500px;font-size:16.5px">
    <div class="slogan__line1">MI PROYECTO DEBE DE SER</div>
    <div class="slogan__line2">REALIZADO 100% EN ESPAÑOL</div>
  </div>
  <div class="abs contact" style="left:221px;top:545px">
    <svg width="8" height="8" viewBox="0 0 10 10"><path d="M2 .8l1.8 2-1 1.2a6 6 0 003.2 3.2l1.2-1 2 1.8-1 1.6C4.6 9.4.6 5.4.4 1.8z" fill="#e5a23a"/></svg>
    <span class="contact__phone" style="font-size:9.5px">(81) 8157-6203</span>
    <svg width="7" height="5" viewBox="0 0 10 7" style="margin-left:6px"><rect width="10" height="7" fill="#e5a23a"/></svg>
    <span class="contact__mail">ventas@brivo-lum.com</span>
  </div>

  <div class="abs footer" style="top:561px">
    <span><svg width="6" height="8" viewBox="0 0 6 8"><path d="M3 0a3 3 0 013 3c0 2-3 5-3 5S0 5 0 3a3 3 0 013-3z" fill="#1d1d1d"/></svg>Monterrey, Nuevo León, México</span>
    <span><svg width="7" height="7" viewBox="0 0 10 10"><circle cx="5" cy="5" r="4.3" fill="none" stroke="#1d1d1d" stroke-width="1.2"/><path d="M.7 5h8.6M5 .7v8.6" stroke="#1d1d1d"/></svg>www.brivo-lum.com</span>
    <span style="gap:4px"><i class="dot"></i><i class="dot"></i>BRIVOLUMX</span>
  </div>
</section>

<!-- Back page -->
<section class="page page--back">
  <div class="abs products-head">NUESTROS PRODUCTOS</div>

  <div class="abs tile" role="img" aria-label="Plástico de burbuja rosa y blanco" style="left:17px;top:67px;width:94px;height:92px;background:linear-gradient(135deg,#f2f2f4,#e6a3b6 70%,#f0f0f0)"></div>
  <div class="abs tile" role="img" aria-label="Cajas de cartón" style="left:117px;top:67px;width:94px;height:92px;background:linear-gradient(135deg,#f3ede6,#b98d5e)"></div>
  <div class="abs tile" role="img" aria-label="Cintas adhesivas" style="left:216px;top:67px;width:94px;height:92px;background:linear-gradient(135deg,#e9cf52,#f1ebd8 60%,#b89b6a)"></div>
  <div class="abs tile" role="img" aria-label="Clavos en rollo" style="left:316px;top:67px;width:94px;height:92px;background:linear-gradient(135deg,#f5f5f5,#8f8f8f)"></div>

  <div class="abs tile" role="img" aria-label="Rollos de película estirable" style="left:17px;top:167px;width:94px;height:92px;background:linear-gradient(135deg,#0d1b3a,#e7e1d3 60%,#0d1b3a)"></div>
  <div class="abs tile" role="img" aria-label="Fleje plástico" style="left:117px;top:167px;width:94px;height:92px;background:linear-gradient(135deg,#ffffff,#3b4b46 60%,#f7f7f7)"></div>
  <div class="abs tile" role="img" aria-label="Guantes de algodón con puntos" style="left:216px;top:167px;width:94px;height:92px;background:linear-gradient(135deg,#f5f3ee,#dcd6c8 60%,#e9df55)"></div>
  <div class="abs tile" role="img" aria-label="Tablas de madera" style="left:316px;top:167px;width:94px;height:92px;background:linear-gradient(135deg,#c08b58,#e8c9a0)"></div>

  <div class="abs tile" role="img" aria-label="Rollos de película plástica" style="left:17px;top:266px;width:94px;height:92px;background:linear-gradient(135deg,#ececec,#c9c9c9)"></div>
  <div class="abs tile" role="img" aria-label="Rollo de espuma" style="left:117px;top:266px;width:94px;height:92px;background:linear-gradient(135deg,#ffffff,#e3e3e3)"></div>
  <div class="abs tile" role="img" aria-label="Esquineros de cartón" style="left:216px;top:266px;width:94px;height:92px;background:linear-gradient(135deg,#ffffff,#5b5d60 55%,#ffffff)"></div>
  <div class="abs tile" role="img" aria-label="Tarimas de madera" style="left:316px;top:266px;width:94px;height:92px;background:linear-gradient(135deg,#ececec,#b98a55 60%,#d9d9d9)"></div>

  <div class="abs tile" role="img" aria-label="Clavos en rollo sobre madera" style="left:17px;top:365px;width:194px;height:122px;background:linear-gradient(135deg,#d8c7a6,#8a8171 50%,#e6d3b0)"></div>
  <div class="abs tile" role="img" aria-label="Tarimas apiladas al aire libre" style="left:217px;top:365px;width:193px;height:122px;background:linear-gradient(180deg,#b9cde0 0%,#c9a677 55%,#e9e9e9 100%)"></div>

  <div class="abs brand" style="left:30px;top:504px;width:180px">
    <div class="brand__name">BRIVO-LUM</div>
    <div class="brand__tag">Empaque Industrial</div>
  </div>
  <div class="abs divider" style="left:213px;top:500px;height:46px"></div>
  <div class="abs slogan" style="left:224px;top:496px;font-size:16.5px">
    <div class="slogan__line1">MI PROYECTO DEBE DE SER</div>
    <div class="slogan__line2">REALIZADO 100% EN ESPAÑOL</div>
  </div>
  <div class="abs contact" style="left:224px;top:541px">
    <svg width="8" height="8" viewBox="0 0 10 10"><path d="M2 .8l1.8 2-1 1.2a6 6 0 003.2 3.2l1.2-1 2 1.8-1 1.6C4.6 9.4.6 5.4.4 1.8z" fill="#e5a23a"/></svg>
    <span class="contact__phone" style="font-size:9.5px">(81) 8157-6203</span>
    <svg width="7" height="5" viewBox="0 0 10 7" style="margin-left:6px"><rect width="10" height="7" fill="#e5a23a"/></svg>
    <span class="contact__mail">ventas@brivo-lum.com</span>
  </div>

  <div class="abs footer" style="top:558px;height:26px">
    <span><svg width="6" height="8" viewBox="0 0 6 8"><path d="M3 0a3 3 0 013 3c0 2-3 5-3 5S0 5 0 3a3 3 0 013-3z" fill="#1d1d1d"/></svg>Monterrey, Nuevo León, México</span>
    <span><svg width="7" height="7" viewBox="0 0 10 10"><circle cx="5" cy="5" r="4.3" fill="none" stroke="#1d1d1d" stroke-width="1.2"/><path d="M.7 5h8.6M5 .7v8.6" stroke="#1d1d1d"/></svg>www.brivo-lum.com</span>
    <span style="gap:4px"><i class="dot"></i><i class="dot"></i>BRIVOLUMX</span>
  </div>
</section>

</body>
</html>
```